Private Practice Dietitian's Business Card

A 2-sided business card for a dietitian (medical nutritionist) in private practice within a natural therapies allied health clinic. The business card needs to imply warmth and professionalism.
Target Market(s)
Doctors who may refer patients to a dietitian and patients themselves who may request dietetic assessment, education and counselling.
Industry/Entity Type
Business
Requirements
Must have
- The business card must be an intense blue on the front at the bottom, gradually lightening towards the top of the card. Please see:
http://pinboardly.example/rupert_halvane/card-ideas/
for an example from "The quiet of the riverbank" book. I'd like an apple tree on the left with a pale silver/grey trunk (like the silver in the book cover)and branches that bends over to the right above the writing. Apples to be a turquoise/aqua colour similar to that in "The quiet of the riverbank" book cover. Front cover writing to read:
foodsteps
0462 883 917
foodsteps@kelvanet.example
'foodsteps' is one word but I would like the 'my' in turquoise/aqua to match the apples and the 'dietitian' and the phone number and email address in the pale silver/grey to match the tree trunk.
I'd like the foodsteps in larger font than the phone number and email address but for all 3 lines of text on the front of the business card to be stretched so they have the same left and right margin. (I hope this makes sense!)
I would like the back of the card to be white and the top section of text to be in the same turquoise/aqua from the apples on the front of the card and to read:
MAREE TOLVIN
Accredited Practising Dietitian (APD)
Bachelor of Health Science (Nutrition & Dietetics) - Honours
Master of Nutrition & Dietetics
This text should be stretched/compacted so that it all has the same left and right margin.
After this text there should be a blank line for spacing before the next section of text, which is to be in the silver/grey of the tree trunk. It should read:
Weight management
Diabetes
Impaired fasting glycaemia
Impaired glucose tolerance
Gestational diabetes
Wellness & general nutrition
Cardiovascular disease
high blood pressure
High cholesterol
High triglycerides
Fatty liver
Constipation
Diverticular disease
Coeliac disease
Irritable bowel syndrome
Gastroesophageal reflux
Lactose intolerance
Gout
Polycystic ovarian syndrome
Fertility
Pregnancy
Breastfeeding
Osteoporosis
Iron deficiency
Vegetarian eating
This set of text can run across the page from left to right and each medical condition could be separated from the next in some way to help with ease of reading. For example perhaps a space, dot and another space could separate the medical conditions. This set of text should be stretched so that the left and right margins of each line is the same. Thank you!
Nice to have
- An easy-to read but 'elegant' font would be nice - but I have no idea which one! Nothing too ornate, but not dull standard Times New Roman/Arial/Comic Sans either!
Should not have
- Times new roman/comic sans/arial fonts

```html
<!DOCTYPE html>
<html lang="en">
<head>
<meta charset="utf-8">
<title>foodsteps – business card</title>
<link href="https://fonts.googleapis.com/css2?family=Lato:wght@400;700&display=swap" rel="stylesheet">
<style>
  :root {
    --navy-deep: #1c2590;
    --navy-top: #3a3f9c;
    --band-dark: #2a4fb4;
    --band-light: #9bb8ec;
    --emblem: #2a2466;
    --silver: #e6ebf5;
    --ink-blue: #1d2c9e;
    --ink-mid: #3a48c0;
    --list-ink: #26318f;
    --outline: #8c8c8c;
    --paper: #ffffff;
  }
  * { box-sizing: border-box; margin: 0; padding: 0; }
  html, body {
    width: 1200px; height: 778px; overflow: hidden;
    background: var(--paper);
    font-family: "Lato", sans-serif;
  }
  .sheet { position: relative; width: 1200px; height: 778px; }

  .card { position: absolute; overflow: hidden; }

  /* Front */
  .card-front {
    left: 10px; top: 66px; width: 590px; height: 324px;
    border-radius: 44px 0 0 44px;
    background: linear-gradient(180deg, var(--navy-top) 0%, #2a3196 45%, var(--navy-deep) 100%);
  }
  .band {
    position: absolute; left: 0; right: 0;
    background: linear-gradient(180deg, var(--band-dark) 0%, #6f93dc 35%, var(--band-light) 52%, #5e83d2 72%, var(--band-dark) 100%);
  }
  .card-front .band { top: 124px; height: 70px; }
  .emblem {
    position: absolute; border-radius: 50%;
    background: radial-gradient(circle at 50% 45%, #3b3488 0%, var(--emblem) 70%);
    border: 3px solid var(--silver);
  }
  .card-front .emblem { left: 88px; top: 62px; width: 184px; height: 184px; }
  .brand-name {
    position: absolute; color: var(--silver);
    font-weight: 400; letter-spacing: 1px; line-height: 1;
  }
  .card-front .brand-name { left: 292px; top: 132px; font-size: 54px; }
  .contact {
    position: absolute; left: 304px; width: 260px;
    color: var(--silver); text-align: justify; text-align-last: justify;
  }
  .contact-phone { top: 250px; font-size: 25px; letter-spacing: 3px; }
  .contact-email { top: 283px; font-size: 19px; }

  /* Back – services */
  .card-services {
    left: 600px; top: 66px; width: 580px; height: 324px;
    border: 1.5px solid var(--outline); border-left: none;
    border-radius: 0 44px 44px 0;
    background: var(--paper);
  }
  .service-list {
    position: absolute; left: 40px; right: 40px; top: 44px;
    list-style: none; text-align: center;
    color: var(--list-ink); font-size: 14.5px; letter-spacing: 2px; line-height: 20px;
  }
  .service-list b { font-weight: 700; }

  /* Back – credentials */
  .card-credentials {
    left: 580px; top: 430px; width: 600px; height: 320px;
    border: 1.5px solid var(--outline);
    border-radius: 44px 16px 16px 44px;
    background: var(--paper);
  }
  .credentials {
    position: absolute; left: 210px; width: 340px; top: 36px;
    text-align: center; line-height: 1.2;
  }
  .credentials .name { color: var(--ink-blue); font-size: 18px; font-weight: 700; letter-spacing: 1px; margin-bottom: 8px; }
  .credentials p { color: var(--ink-mid); font-size: 15.5px; }
  .card-credentials .band { top: 150px; height: 58px; }
  .card-credentials .emblem { left: 20px; top: 100px; width: 180px; height: 180px; }
  .card-credentials .brand-name { left: 222px; top: 154px; font-size: 50px; }
</style>
</head>
<body>
<main class="sheet">

  <section class="card card-front" aria-label="Card front">
    <div class="band"></div>
    <div class="emblem" role="img" aria-label="Apple tree illustration with silver trunk and aqua apples"></div>
    <span class="brand-name">foodsteps</span>
    <div class="contact contact-phone">0462 883 917</div>
    <div class="contact contact-email">foodsteps@kelvanet.example</div>
  </section>

  <section class="card card-services" aria-label="Card back, areas of practice">
    <ul class="service-list">
      <li><b>W</b>eight management &nbsp;<b>D</b>iabetes</li>
      <li><b>I</b>mpaired fasting glycaemia</li>
      <li><b>I</b>mpaired glucose tolerance</li>
      <li><b>G</b>estational diabetes <b>W</b>ellness &amp; general nutrition</li>
      <li><b>C</b>ardiovascular disease <b>H</b>igh blood pressure</li>
      <li><b>H</b>igh cholesterol <b>H</b>igh triglycerides</li>
      <li><b>F</b>atty liver &nbsp;<b>C</b>onstipation <b>D</b>iverticular disease</li>
      <li><b>C</b>oeliac disease &nbsp;<b>I</b>rritable bowel syndrome</li>
      <li><b>G</b>astroesophageal reflux &nbsp;<b>L</b>actose intolerance</li>
      <li><b>G</b>out <b>P</b>olycystic ovarian syndrome <b>F</b>ertility</li>
      <li><b>P</b>regnancy &nbsp;<b>B</b>reastfeeding &nbsp;<b>O</b>steoporosis</li>
      <li><b>I</b>ron deficiency &nbsp;<b>V</b>egetarian eating</li>
    </ul>
  </section>

  <section class="card card-credentials" aria-label="Card back, practitioner details">
    <div class="credentials">
      <h1 class="name">MAREE TOLVIN</h1>
      <p>Accredited Practising Dietitian (APD)</p>
      <p>Bachelor of Health Science<br>(Nutrition &amp; Dietetics) - Honours</p>
      <p>Master of Nutrition &amp; Dietetics</p>
    </div>
    <div class="band"></div>
    <div class="emblem" role="img" aria-label="Apple tree illustration with silver trunk and aqua apples"></div>
    <span class="brand-name">foodsteps</span>
  </section>

</main>
</body>
</html>
```